Tall Harbor Business Card

We are a Video Production and Video Equipment Rental company specialising in the supply of state of the art Video Technology and Services for the Live Entertainment, Television and Corporate Business Theatre markets. (in Sydney, Australia) www.tallharbor.example

Industry/Entity Type

Business

Contact Information for Business Card

name, position, email, website, address, logo
Example attached of the information we need - doesn't necessarily have to look the same

Font styles to use
Other font styles liked:
• Tall Harbor logo font is GOTHAM

Colors
ea1f27

Requirements
Nice to have
• either matt black or shiny black cards -
raised logo

```html
<!DOCTYPE html>
<html lang="en">
<head>
<meta charset="utf-8">
<title>Tall Harbor Business Card</title>
<link rel="stylesheet" href="https://fonts.googleapis.com/css2?family=Lato:wght@400;700&display=swap">
<style>
  :root {
    --backdrop: #8c4c25;
    --card-black: #1b1b1d;
    --card-edge: #232326;
    --brand-red: #ea1f27;
    --ink-white: #ffffff;
    --ink-soft: #e6e6e6;
  }
  * { margin: 0; padding: 0; box-sizing: border-box; }
  html, body {
    width: 1200px; height: 800px; overflow: hidden;
    background: var(--backdrop);
    font-family: "Lato", Arial, sans-serif;
  }
  .canvas { position: relative; width: 1200px; height: 800px; }

  .card {
    position: absolute; left: 266px; width: 514px; height: 300px;
    border-radius: 14px; overflow: hidden;
    background: radial-gradient(circle at 50% 35%, var(--card-edge), var(--card-black) 75%);
    box-shadow: 0 6px 14px rgba(0,0,0,0.35);
  }
  .card--front { top: 113px; }
  .card--back { top: 428px; }

  .stripe-white {
    position: absolute; left: 0; right: 0; top: 275px; height: 5px;
    background: var(--ink-white);
  }
  .stripe-red {
    position: absolute; left: 0; right: 0; top: 284px; height: 16px;
    background: var(--brand-red);
  }

  .wordmark {
    position: absolute; display: flex; align-items: center; gap: 12px;
    color: var(--ink-white); font-weight: 700; letter-spacing: 0.5px; white-space: nowrap;
  }
  .wordmark__square { background: var(--brand-red); flex: none; }
  .card--front .wordmark { left: 0; right: 0; justify-content: center; top: 92px; font-size: 40px; }
  .card--front .wordmark__square { width: 14px; height: 14px; }
  .card--back .wordmark { left: 46px; top: 55px; font-size: 32px; }
  .card--back .wordmark__square { width: 12px; height: 12px; }

  .services {
    position: absolute; left: 0; right: 0; top: 170px;
    text-align: center; color: var(--ink-white); font-size: 13.5px;
  }

  .person { position: absolute; right: 42px; top: 130px; text-align: right; }
  .person__name { color: var(--brand-red); font-weight: 700; font-size: 17px; letter-spacing: 0.3px; }
  .person__role { color: var(--ink-white); font-size: 13.5px; margin-top: 1px; }

  .contacts { position: absolute; left: 46px; top: 198px; list-style: none; }
  .contacts li {
    display: flex; align-items: center; gap: 8px;
    color: var(--ink-soft); font-size: 13.5px; height: 20.5px;
  }
  .contacts svg { width: 12px; height: 12px; fill: var(--brand-red); flex: none; }
</style>
</head>
<body>
<main class="canvas">
  <section class="card card--front" aria-label="Business card front">
    <div class="wordmark"><span class="wordmark__square"></span>TALL HARBOR</div>
    <p class="services">Video Solutions - LED Screens - Camera Systems - Projection</p>
    <div class="stripe-white"></div>
    <div class="stripe-red"></div>
  </section>

  <section class="card card--back" aria-label="Business card back">
    <div class="wordmark"><span class="wordmark__square"></span>TALL HARBOR</div>
    <div class="person">
      <p class="person__name">SAM FERRANTE</p>
      <p class="person__role">Managing Director</p>
    </div>
    <ul class="contacts">
      <li>
        <svg viewBox="0 0 12 12" aria-hidden="true"><path d="M0 2h12v8H0z M0 2l6 4 6-4v1.4L6 7.4 0 3.4z" fill-rule="evenodd"/></svg>
        sam@tallharbor.example
      </li>
      <li>
        <svg viewBox="0 0 12 12" aria-hidden="true"><path d="M6 0a6 6 0 1 0 0 12A6 6 0 0 0 6 0zm0 1.3c.8.8 1.4 2.4 1.5 4H4.5C4.6 3.7 5.2 2.1 6 1.3zM1.4 5.3c.2-1.8 1.5-3.3 3.1-3.8-.6.9-1 2.3-1.1 3.8zm0 1.4h2c.1 1.5.5 2.9 1.1 3.8-1.6-.5-2.9-2-3.1-3.8zM6 10.7c-.8-.8-1.4-2.4-1.5-4h3c-.1 1.6-.7 3.2-1.5 4zm1.5-.2c.6-.9 1-2.3 1.1-3.8h2c-.2 1.8-1.5 3.3-3.1 3.8zm1.1-5.2c-.1-1.5-.5-2.9-1.1-3.8 1.6.5 2.9 2 3.1 3.8z"/></svg>
        www.tallharbor.example
      </li>
      <li>
        <svg viewBox="0 0 12 12" aria-hidden="true"><path d="M6 0a4.2 4.2 0 0 0-4.2 4.2C1.8 7.4 6 12 6 12s4.2-4.6 4.2-7.8A4.2 4.2 0 0 0 6 0zm0 5.8a1.6 1.6 0 1 1 0-3.2 1.6 1.6 0 0 1 0 3.2z"/></svg>
        12 Wren Lane, Mascot, NSW 2020 Australia
      </li>
    </ul>
    <div class="stripe-white"></div>
    <div class="stripe-red"></div>
  </section>
</main>
</body>
</html>
```